Brisk Ember - Stock Certificate

We need a custom designed stock certificate that represents the look of our company logo but also have a cool look compared to a standard stock certificate. We thinking we want the logo in gold. Our website is https://www.briskemberusa.example.

We are wanting the certificate to look very professional and really cool, we have sales agents that work for the company and we are creating a program by which the sales agents can gain ownership in the company. So the certificates need to have a very cool appeal and that provides a sense of pride in owning "Units" in Brisk Ember.

Reason: Extending so other board members can vote as well, thank you all!

Target Market(s)

Stock/Shareholders

Industry/Entity Type

It Company

Font styles to use
Script

Requirements
Must have
• Must look like a stock certificate, must use our logo which the psd file for it was attached.
Nice to have
• Nice to have the logo in gold

```html
<!DOCTYPE html>
<html lang="en">
<head>
<meta charset="utf-8">
<title>Brisk Ember – Stock Certificate</title>
<link href="https://fonts.googleapis.com/css2?family=UnifrakturMaguntia&family=Great+Vibes&family=Arimo:wght@400;700&display=swap" rel="stylesheet">
<style>
  :root {
    --backdrop: #b9adb8;
    --paper: #f6f6f6;
    --paper-shade: #ececec;
    --frame-deep: #d9480f;
    --frame-mid: #f07a12;
    --frame-light: #f5d21a;
    --title: #c8461a;
    --ink: #1d1d1d;
    --fill-ink: #8a6a4a;
    --rule: #2a2a2a;
    --atom-core: #f4a018;
  }
  * { box-sizing: border-box; margin: 0; padding: 0; }
  html, body { width: 1200px; height: 960px; overflow: hidden; }
  body {
    background: var(--backdrop);
    font-family: "Arimo", Arial, sans-serif;
    color: var(--ink);
    position: relative;
  }
  .certificate {
    position: absolute;
    left: 60px; top: 100px;
    width: 1080px; height: 760px;
    background: linear-gradient(135deg, var(--paper) 0%, var(--paper-shade) 100%);
    box-shadow: 0 18px 40px rgba(60, 40, 60, 0.35);
  }
  .certificate__frame {
    position: absolute; inset: 0;
    width: 100%; height: 100%;
  }
  .certificate__map {
    position: absolute;
    left: 120px; top: 80px; width: 840px; height: 600px;
    background: radial-gradient(ellipse at center, rgba(200,200,200,0.45) 0%, rgba(220,220,220,0.15) 60%, rgba(255,255,255,0) 80%);
  }
  .brand {
    position: absolute;
    left: 100px; top: 140px;
    width: 260px;
  }
  .brand__emblem {
    width: 220px; height: 190px;
    border-radius: 50%;
    background: radial-gradient(circle at 50% 55%, #fff3b0 0%, var(--atom-core) 25%, #c9620f 55%, rgba(138,58,12,0.25) 75%, rgba(255,255,255,0) 100%);
  }
  .brand__name {
    display: flex; align-items: center; gap: 10px;
    margin-top: 22px;
    font-size: 32px; font-weight: 400;
    color: var(--ink);
    letter-spacing: 1px;
    white-space: nowrap;
  }
  .brand__mark {
    width: 14px; height: 14px;
    background: var(--frame-mid);
  }
  .title {
    position: absolute;
    left: 430px; top: 150px; width: 560px;
    text-align: center;
    font-family: "UnifrakturMaguntia", serif;
    font-size: 76px;
    color: var(--title);
    font-weight: 400;
  }
  .body {
    position: absolute;
    left: 400px; top: 270px; width: 620px;
    font-size: 16px; line-height: 30px;
  }
  .body__lead {
    margin-left: 90px; width: 440px;
    text-align: center;
  }
  .holder {
    display: block;
    margin: 2px 0 6px 90px;
    width: 440px;
    border-bottom: 1px solid var(--rule);
    font-family: "Great Vibes", cursive;
    font-size: 58px; line-height: 64px;
    text-align: center;
  }
  .body__line { white-space: nowrap; }
  .body__line--gap { margin-top: 8px; }
  .fill {
    display: inline-block;
    border-bottom: 1px solid var(--rule);
    font-family: "Great Vibes", cursive;
    color: var(--fill-ink);
    font-size: 22px;
    text-align: center;
    line-height: 24px;
  }
  .fill--count { width: 56px; }
  .fill--par { width: 100px; }
  .fill--class { width: 140px; font-size: 18px; color: var(--ink); }
  .signatures {
    position: absolute;
    left: 160px; right: 160px; top: 580px;
    display: flex; justify-content: space-between;
  }
  .signature { width: 220px; text-align: center; }
  .signature__mark {
    height: 44px; width: 120px; margin: 0 auto;
    background: linear-gradient(90deg, rgba(40,40,40,0) 0%, rgba(40,40,40,0.25) 50%, rgba(40,40,40,0) 100%);
    border-radius: 40%;
  }
  .signature__line { border-top: 1px solid var(--rule); margin-top: 4px; }
  .signature__label {
    font-family: "Great Vibes", cursive;
    font-size: 22px;
  }
  .signature--second { margin-top: 50px; }
</style>
</head>
<body>
  <main class="certificate">
    <svg class="certificate__frame" viewBox="0 0 1080 760" aria-hidden="true">
      <defs>
        <linearGradient id="frameGradient" x1="0" y1="0" x2="1" y2="1">
          <stop offset="0" stop-color="#d9480f"/>
          <stop offset="0.45" stop-color="#f07a12"/>
          <stop offset="0.75" stop-color="#d9480f"/>
          <stop offset="1" stop-color="#f5d21a"/>
        </linearGradient>
      </defs>
      <path d="M70 30 H1010 A40 40 0 0 0 1050 70 V690 A40 40 0 0 0 1010 730 H70 A40 40 0 0 0 30 690 V70 A40 40 0 0 0 70 30 Z"
            fill="none" stroke="url(#frameGradient)" stroke-width="6"/>
    </svg>

    <div class="certificate__map" role="img" aria-label="Faint world map in the background"></div>

    <div class="brand">
      <div class="brand__emblem" role="img" aria-label="Glowing golden atom illustration"></div>
      <div class="brand__name"><span class="brand__mark"></span>Brisk Ember</div>
    </div>

    <h1 class="title">Stock Certificate</h1>

    <section class="body">
      <div class="body__lead">This certifies that</div>
      <span class="holder">John Doe</span>
      <div class="body__line">is entitled to <span class="fill fill--count">55</span> shares of the par value of <span class="fill fill--par">120$</span> each of the</div>
      <div class="body__line"><span class="fill fill--class">Common stock</span> of the Brisk Ember Company</div>
      <div class="body__line">transferable in person or by Attorney only in the books of the Company</div>
      <div class="body__line">and upon the surrender of this Certificate.</div>
      <div class="body__line body__line--gap">In witness whereof the Brisk Ember Company has caused this Certificate to be</div>
    </section>

    <div class="signatures">
      <div class="signature">
        <div class="signature__mark" role="img" aria-label="Handwritten signature"></div>
        <div class="signature__line"></div>
        <div class="signature__label">Signature</div>
      </div>
      <div class="signature signature--second">
        <div class="signature__mark" role="img" aria-label="Handwritten signature"></div>
        <div class="signature__line"></div>
        <div class="signature__label">Signature</div>
      </div>
    </div>
  </main>
</body>
</html>
```